2 page brouchure for a Property Valuation company.

We require a 2 page brochure (printed front and back) for a property valuation company known as 'Quorvel Valuations'.

Quorvel valuations provides independent, reliable, accurate valuation services to our clients on the value of their properties to enable confidence and certainty in their decision.

The brochure is to be used to convey that the company provides valuation services for 8 main purposes and across 4 different property types.

The 8 main purposes for valuation include:
- Pre-Purchase Valuations
- Stamp Duty Valuations
-Capital Gains Tax (CGT)Valuations
-Unit Entitlement Valuations
-Family Law and Litigation Valuations
-Easement Valuations
-Wills & Probate Valuations
-Insolvency/Asset Realisation Valuations

The 4 main property types are:
-Residential
-Commercial
-Industrial
-Retail.

The brochure should have a title page, a page for the services, a page for the property types and a rear page with contact details.
Contact detail will include;
email:
phone :
Post :
website:

The words 'property valuation and advisory services' should be used at the front of the brochure.

The brochure should be professional and is used to convey information using visual aid and is to be used for promotion.

Our main colors are dark green and grey as seen in our logo.

We have attached our logo to add to the brochure and visit our website at: www.quorvelvaluations-example.com.au for more information about the company.

Please let me know if there are any further questions.

Target Market(s)

Solicitors/Lawyers
Accountants
Surveyors
Builders/Developers

Requirements
Must have
• Logo Colors, Logo, 8 Main services, 4 main property types, contact details.
Nice to have
• Should have concise visual aids to convey message.

Please add that we provide fast 48 hour turnaround for short form valuations. Maybe use a visual aid to convey this.

```html
<!DOCTYPE html>
<html lang="en">
<head>
<meta charset="utf-8">
<title>Quorvel Valuations – Brochure</title>
<link href="https://fonts.googleapis.com/css2?family=Oswald:wght@600;700&family=Montserrat:wght@400;500;600&family=Roboto:wght@400;700&display=swap" rel="stylesheet">
<style>
  :root{
    --green:#176b45;
    --green-dark:#0f5a38;
    --grey-bg:#9a9a9a;
    --ink:#2c2c2c;
    --text:#3a3a3a;
    --ring:#3b3b3b;
    --white:#ffffff;
  }
  *{box-sizing:border-box;margin:0;padding:0}
  html,body{width:1200px;height:960px;overflow:hidden}
  body{background:var(--grey-bg);position:relative;font-family:"Roboto",sans-serif;color:var(--text)}

  .sheet-title{position:absolute;left:49px;top:30px}
  .sheet-title h1{font-family:"Montserrat",sans-serif;font-weight:600;font-size:52px;letter-spacing:-1px;color:#262626;line-height:1;-webkit-text-stroke:1.5px #262626}
  .sheet-title p{font-family:"Montserrat",sans-serif;font-weight:400;font-size:28px;color:#333;margin-top:10px;letter-spacing:.5px}

  .page{position:absolute;top:166px;width:528px;height:744px;background:var(--white);overflow:hidden;box-shadow:4px 6px 10px rgba(0,0,0,.35)}
  .page--front{left:50px}
  .page--back{left:622px}

  /* front */
  .hero-photo{position:absolute;left:0;top:0;width:528px;height:262px;
    background:linear-gradient(180deg,rgba(255,255,255,0) 55%,#fff 100%),linear-gradient(100deg,#a7b0ad 0%,#c9d0cf 35%,#b6bcb6 60%,#dfe3e1 100%)}
  .hero-title{position:absolute;left:36px;top:30px;font-family:"Oswald",sans-serif;font-weight:700;font-size:44px;line-height:50px;letter-spacing:-.5px}
  .hero-title .line-1{color:var(--green);display:block;text-shadow:1px 1px 2px rgba(255,255,255,.6)}
  .hero-title .line-2{color:var(--white);display:block;text-shadow:2px 2px 3px rgba(0,0,0,.55)}

  .services-tab{position:absolute;left:0;top:270px;width:72px;height:184px;background:var(--green);display:flex;align-items:center;justify-content:center}
  .services-tab span{transform:rotate(-90deg);color:#fff;font-family:"Roboto",sans-serif;font-weight:700;font-size:32px;white-space:nowrap}

  .service{position:absolute;width:110px;margin-left:-55px;text-align:center;font-size:12.5px;line-height:15px;color:var(--text)}
  .service svg{display:block;margin:0 auto 6px;width:30px;height:30px}

  .types-bar{position:absolute;left:0;top:485px;width:277px;height:58px;background:var(--green);color:#fff;font-family:"Montserrat",sans-serif;font-weight:600;font-size:30px;line-height:58px;padding-left:28px}

  .ptype{position:absolute;width:90px;margin-left:-45px;text-align:center;font-size:12.5px;color:var(--text)}
  .ptype svg{display:block;margin:0 auto 10px;width:29px;height:29px}

  .brand{position:absolute;left:40px;top:663px;display:flex;align-items:center;gap:14px}
  .brand-mark{width:50px;height:50px;background:var(--green)}
  .brand-name{font-family:"Montserrat",sans-serif;font-weight:500;font-size:20px;letter-spacing:4px;line-height:21px;color:#333}

  .corner-band{position:absolute;left:0;top:0;width:528px;height:744px}
  .badge{position:absolute;left:372px;top:540px;width:120px;height:200px;text-align:center;color:#fff}
  .badge svg{display:block;width:120px;height:135px}
  .badge .t1{font-family:"Oswald",sans-serif;font-weight:700;font-size:17px;line-height:18px;margin-top:4px}
  .badge .t2{font-size:11.5px;line-height:13px}

  /* back */
  .back-photo{position:absolute;left:0;top:0;width:528px;height:253px;background:linear-gradient(180deg,#55585c 0%,#8d9195 55%,#dcdfe1 100%)}
  .form-title{position:absolute;left:108px;top:216px;width:311px;height:74px;background:#fff;box-shadow:0 4px 8px rgba(0,0,0,.3);font-family:"Oswald",sans-serif;font-weight:700;font-size:37px;color:var(--ink);text-align:center;line-height:74px;letter-spacing:.5px}
  .field{position:absolute;left:44px;width:439px;height:14px;font-size:12px;color:var(--text)}
  .field svg{position:absolute;left:0;top:1px;width:11px;height:11px}
  .field span{position:absolute;left:19px;top:0}
  .field::after{content:"";position:absolute;left:19px;right:0;top:16px;border-bottom:1px solid #555}
  .about{position:absolute;left:44px;top:557px;width:290px;font-size:12.2px;line-height:19.5px;color:var(--text)}
</style>
</head>
<body>

<header class="sheet-title">
  <h1>PREVIEW</h1>
  <p>Brochure/Flyer Design</p>
</header>

<!-- FRONT PAGE -->
<section class="page page--front">
  <div class="hero-photo" role="img" aria-label="Photo of a smiling family relaxing on a lawn in front of a modern glass house"></div>
  <h2 class="hero-title"><span class="line-1">PROPERTY VALUATION</span><span class="line-2">&amp; ADVISORY SERVICES</span></h2>

  <svg class="corner-band" viewBox="0 0 528 744" aria-hidden="true">
    <defs>
      <linearGradient id="fadeFront" x1="1" y1="0" x2="0.6" y2="0.5">
        <stop offset="0" stop-color="#176b45" stop-opacity=".35"/>
        <stop offset="1" stop-color="#176b45" stop-opacity="0"/>
      </linearGradient>
    </defs>
    <polygon points="220,744 528,440 528,744" fill="url(#fadeFront)"/>
    <polygon points="274,744 528,498 528,744" fill="#176b45"/>
  </svg>

  <div class="services-tab"><span>Services</span></div>

  <div class="service" style="left:145px;top:276px">
    <svg viewBox="0 0 30 30"><rect x="2" y="2" width="26" height="26" rx="3" fill="none" stroke="#176b45" stroke-width="2"/><path d="M8 15l5 5 9-10" fill="none" stroke="#176b45" stroke-width="2"/></svg>
    Pre-Purchase<br>Valuations</div>
  <div class="service" style="left:247px;top:276px">
    <svg viewBox="0 0 30 30"><rect x="2" y="2" width="26" height="26" rx="3" fill="none" stroke="#176b45" stroke-width="2"/><circle cx="15" cy="10" r="3" fill="none" stroke="#176b45" stroke-width="1.8"/><path d="M14 13v4M16 13v4M8 18h14v3H8zM8 24h14" fill="none" stroke="#176b45" stroke-width="1.8"/></svg>
    Stamp Duty<br>Valuations</div>
  <div class="service" style="left:343px;top:276px">
    <svg viewBox="0 0 30 30"><rect x="2" y="2" width="26" height="26" rx="3" fill="none" stroke="#176b45" stroke-width="2"/><path d="M12 9h6l-1 3c4 2 6 6 5 10H8c-1-4 1-8 5-10z" fill="none" stroke="#176b45" stroke-width="1.8"/><path d="M12 20l6-5" stroke="#176b45" stroke-width="1.5"/></svg>
    Capital Gains<br>Tax (CGT)<br>Valuations</div>
  <div class="service" style="left:439px;top:276px">
    <svg viewBox="0 0 30 30"><rect x="2" y="2" width="26" height="26" rx="3" fill="none" stroke="#176b45" stroke-width="2"/><path d="M6 15l9-8 9 8M9 13v10h12V13M13 23v-5h4v5" fill="none" stroke="#176b45" stroke-width="1.8"/></svg>
    Unit<br>Entitlement<br>Valuations</div>

  <div class="service" style="left:145px;top:368px">
    <svg viewBox="0 0 30 30"><rect x="2" y="2" width="26" height="26" rx="3" fill="none" stroke="#176b45" stroke-width="2"/><circle cx="10" cy="12" r="2.5" fill="none" stroke="#176b45" stroke-width="1.6"/><circle cx="20" cy="12" r="2.5" fill="none" stroke="#176b45" stroke-width="1.6"/><circle cx="15" cy="17" r="2" fill="none" stroke="#176b45" stroke-width="1.6"/><path d="M6 23c0-4 2-6 4-6M24 23c0-4-2-6-4-6M11 24c0-3 2-4 4-4s4 1 4 4" fill="none" stroke="#176b45" stroke-width="1.6"/></svg>
    Family Law<br>and Litigation<br>Valuations</div>
  <div class="service" style="left:247px;top:368px">
    <svg viewBox="0 0 30 30"><rect x="2" y="2" width="26" height="26" rx="3" fill="none" stroke="#176b45" stroke-width="2"/><path d="M15 7l9 5-9 5-9-5zM6 16l9 5 9-5M6 20l9 5 9-5" fill="none" stroke="#176b45" stroke-width="1.7"/></svg>
    Easement<br>Valuations</div>
  <div class="service" style="left:343px;top:372px">
    <svg viewBox="0 0 30 30"><rect x="2" y="2" width="26" height="26" rx="3" fill="none" stroke="#176b45" stroke-width="2"/><path d="M9 6h10l3 3v15H9zM12 11h7M12 15h7M12 19h4" fill="none" stroke="#176b45" stroke-width="1.7"/></svg>
    Wills &amp; Probate<br>Valuations</div>
  <div class="service" style="left:439px;top:368px">
    <svg viewBox="0 0 30 30"><rect x="2" y="2" width="26" height="26" rx="3" fill="none" stroke="#176b45" stroke-width="2"/><path d="M7 7v16h16M10 19l4-5 3 3 5-7M18 10h4v4" fill="none" stroke="#176b45" stroke-width="1.7"/></svg>
    Insolvency/<br>Asset<br>Realisation<br>Valuations</div>

  <div class="types-bar">Property Types</div>

  <div class="ptype" style="left:69px;top:566px">
    <svg viewBox="0 0 29 29"><rect width="29" height="29" rx="3" fill="#176b45"/><path d="M6 14l8.5-7 8.5 7M8.5 12v10h12V12M12.5 22v-5h4v5" fill="none" stroke="#fff" stroke-width="1.6"/></svg>Residential</div>
  <div class="ptype" style="left:151px;top:566px">
    <svg viewBox="0 0 29 29"><rect width="29" height="29" rx="3" fill="#176b45"/><path d="M8 23V6h13v17M6 23h17M11 9h2M16 9h2M11 13h2M16 13h2M11 17h2M16 17h2" fill="none" stroke="#fff" stroke-width="1.6"/></svg>Commercial</div>
  <div class="ptype" style="left:235px;top:566px">
    <svg viewBox="0 0 29 29"><rect width="29" height="29" rx="3" fill="#176b45"/><path d="M6 23V7h3v8l5-4v4l5-4v4l4-3v11zM10 19h2M15 19h2" fill="none" stroke="#fff" stroke-width="1.6"/></svg>Industrial</div>
  <div class="ptype" style="left:318px;top:566px">
    <svg viewBox="0 0 29 29"><rect width="29" height="29" rx="3" fill="#176b45"/><path d="M6 11l2-5h13l2 5zM6 11c0 2 3 2 3.5 0 .5 2 4 2 4.5 0 .5 2 4 2 4.5 0 .5 2 4 2 4.5 0M8 14v9h13v-9M12 23v-5h5v5" fill="none" stroke="#fff" stroke-width="1.5"/></svg>Retail</div>

  <div class="brand">
    <div class="brand-mark"></div>
    <div class="brand-name">QUORVEL<br>VALUATIONS</div>
  </div>

  <div class="badge">
    <svg viewBox="0 0 120 135" aria-hidden="true">
      <rect x="50" y="6" width="20" height="12" rx="3" fill="#3b3b3b"/>
      <rect x="54" y="16" width="12" height="10" fill="#3b3b3b"/>
      <circle cx="60" cy="78" r="50" fill="#3b3b3b"/>
      <circle cx="60" cy="78" r="43" fill="#fff"/>
      <circle cx="60" cy="78" r="40" fill="#176b45"/>
      <circle cx="60" cy="78" r="35" fill="none" stroke="#fff" stroke-width="4" stroke-dasharray="1.5 4"/>
      <text x="60" y="86" text-anchor="middle" font-family="Oswald, sans-serif" font-weight="700" font-size="34" fill="#fff">48</text>
      <text x="60" y="104" text-anchor="middle" font-family="Oswald, sans-serif" font-weight="700" font-size="13" fill="#fff">HOURS</text>
    </svg>
    <div class="t1">TURNAROUND</div>
    <div class="t2">FOR SHORT FORM<br>VALUATIONS</div>
  </div>
</section>

<!-- BACK PAGE -->
<section class="page page--back">
  <div class="back-photo" role="img" aria-label="Photo of a businessman in a suit signing a document beside a small model house"></div>
  <svg class="corner-band" viewBox="0 0 528 744" aria-hidden="true">
    <defs>
      <linearGradient id="fadeBack" x1="1" y1="0" x2="0.6" y2="0.5">
        <stop offset="0" stop-color="#176b45" stop-opacity=".35"/>
        <stop offset="1" stop-color="#176b45" stop-opacity="0"/>
      </linearGradient>
    </defs>
    <polygon points="0,0 254,0 0,246" fill="#176b45"/>
    <polygon points="220,744 528,440 528,744" fill="url(#fadeBack)"/>
    <polygon points="274,744 528,498 528,744" fill="#176b45"/>
  </svg>

  <div class="form-title">CONTACT FORM</div>

  <div class="field" style="top:361px">
    <svg viewBox="0 0 12 12"><rect x="0" y="2" width="12" height="8" fill="#176b45"/><path d="M0 2l6 4 6-4" fill="none" stroke="#fff" stroke-width="1"/></svg>
    <span>Email Address :</span></div>
  <div class="field" style="top:393px">
    <svg viewBox="0 0 12 12"><path d="M2 1l2.5 0 1 3-1.5 1c.8 1.6 1.5 2.3 3 3l1-1.5 3 1V11c-5 .5-9.5-4-9-10z" fill="#176b45"/></svg>
    <span>Phone :</span></div>
  <div class="field" style="top:422px">
    <svg viewBox="0 0 12 12"><path d="M2 0h8v12L6 9 2 12z" fill="#176b45"/></svg>
    <span>Post :</span></div>
  <div class="field" style="top:457px">
    <svg viewBox="0 0 12 12"><circle cx="6" cy="6" r="5.2" fill="none" stroke="#176b45" stroke-width="1.4"/><path d="M1 6h10M6 1c-2.5 3-2.5 7 0 10M6 1c2.5 3 2.5 7 0 10" fill="none" stroke="#176b45" stroke-width="1"/></svg>
    <span>Website :</span></div>

  <p class="about">Quorvel valuations provides independent, reliable, accurate valuation services to our clients on the value of their properties to enable confidence and certainty in their decision.</p>

  <div class="brand" style="left:38px">
    <div class="brand-mark"></div>
    <div class="brand-name">QUORVEL<br>VALUATIONS</div>
  </div>

  <div class="badge">
    <svg viewBox="0 0 120 135" aria-hidden="true">
      <rect x="50" y="6" width="20" height="12" rx="3" fill="#3b3b3b"/>
      <rect x="54" y="16" width="12" height="10" fill="#3b3b3b"/>
      <circle cx="60" cy="78" r="50" fill="#3b3b3b"/>
      <circle cx="60" cy="78" r="43" fill="#fff"/>
      <circle cx="60" cy="78" r="40" fill="#176b45"/>
      <circle cx="60" cy="78" r="35" fill="none" stroke="#fff" stroke-width="4" stroke-dasharray="1.5 4"/>
      <text x="60" y="86" text-anchor="middle" font-family="Oswald, sans-serif" font-weight="700" font-size="34" fill="#fff">48</text>
      <text x="60" y="104" text-anchor="middle" font-family="Oswald, sans-serif" font-weight="700" font-size="13" fill="#fff">HOURS</text>
    </svg>
    <div class="t1">TURNAROUND</div>
    <div class="t2">FOR SHORT FORM<br>VALUATIONS</div>
  </div>
</section>

</body>
</html>
```